Wordpress Design Project

Word press design for speaker/writer to blog and let audience know what I'm doing, who I am and what my message is about.
I've written a couple of books and intend to promote my books, articles/blogs and video blogs on this site.
I would like to have an about me tab, rotating pictures in the header, (not sure I'm describing that correctly, but the following is a link that shows you what I mean) :
http://velmostra.com/simplymarla/2013/01/30/hello-world/
I'd like to have the share this buttons for all the social media sites (probably a widget?), as well as the stats on how often the link, video or article was shared.
Updates
Project Deadline Extended
Reason: My timeframes have been moved out because the marketing media event that caused me to need this site immediately has been moved out a couple of days. Hopeully there is more time to have more designers submit now.
Target Market(s)
Mainly women 30+
Industry/Entity Type
Media
Requirements
Must have
- My Simply Marla logo needs to be on the site and I'd like to have the share this buttons for all the social media sites (probably a widget?), as well as the stats on how often the link, video or article was shared. I'd like to be able to see the comments and be able to maintain the site myself as well as swap out the pictures if I so desire.
I added files, but they are png, let me know if you need the ai files.
I'd like to be able to add tabs later if I decide so I'd like the template to be flexible enough that I can add a tab without compromising the look and feel of the site.
I also want to be able to upload my videos to the site.

```html
<!DOCTYPE html>
<html lang="en">
<head>
<meta charset="utf-8">
<title>Simply Marla</title>
<link href="https://fonts.googleapis.com/css2?family=Open+Sans:wght@400;600;700&family=Droid+Serif&display=swap" rel="stylesheet">
<style>
:root{
  --page:#eeeeee;
  --panel:#ffffff;
  --ink:#333333;
  --muted:#8a8a8a;
  --line:#dddddd;
  --orange:#f88c00;
  --dark:#2d2d2d;
  --bar:#e8e8e8;
  --blue:#4a6aa0;
  --red:#d9412f;
}
*{box-sizing:border-box;margin:0;padding:0}
html,body{width:1200px;height:2492px;overflow:hidden}
body{background:var(--page);font-family:"Open Sans",Arial,sans-serif;color:var(--ink);position:relative}
.abs{position:absolute}
.shell{left:47px;top:44px;width:1100px;height:2328px;background:#f7f7f7}
.topbar{left:128px;top:64px;width:935px;height:28px;background:#fafafa;border-bottom:4px solid var(--orange);display:flex;align-items:center;padding:0 6px;font-size:11px;color:var(--muted)}
.topbar .date{background:#e6e6e6;padding:3px 10px;margin-right:18px;font-size:10px}
.socials{display:flex;gap:2px;margin-left:auto}
.socials span{width:15px;height:15px;background:#9a9a9a;display:block}
.header{left:128px;top:98px;width:935px;height:318px;background:linear-gradient(180deg,#ffffff 0%,#ffffff 48%,#6a7590 60%,#000000 70%,#000000 100%);border-bottom:4px solid var(--blue)}
.brand{position:absolute;left:50px;top:110px;font-family:"Droid Serif",Georgia,serif;font-size:56px;color:#111}
.portrait{position:absolute;left:699px;top:39px;width:176px;height:172px;background:linear-gradient(160deg,#6b5a48,#2d241c);border:3px solid #eee}
.nav{left:128px;top:424px;width:935px;height:47px;background:var(--dark);border-bottom:4px solid var(--orange);display:flex;align-items:center}
.nav .home{width:44px;height:43px;background:var(--orange);display:flex;align-items:center;justify-content:center;margin:0 12px 0 8px}
.nav a{color:#e4e4e4;font-size:12px;text-decoration:none;padding:0 11px}
.main{left:128px;top:487px;width:935px;height:1866px;background:var(--panel);border:1px solid #e4e4e4}
.slider{left:150px;top:502px;width:591px;height:298px;background:linear-gradient(180deg,#8fbf6a 0%,#3f7a2f 60%,#2e5a1f 100%)}
.slider .cap{position:absolute;left:128px;bottom:16px;width:463px;height:72px;background:rgba(0,0,0,.7);color:#fff;padding:8px 10px}
.slider .cap h3{font-size:17px;font-weight:600;margin-bottom:4px}
.slider .cap p{font-size:11px;line-height:1.35}
.slider .track{position:absolute;left:0;bottom:0;width:591px;height:6px;background:#555}
.slider .track i{position:absolute;left:118px;top:0;width:118px;height:6px;background:var(--orange)}
.head{display:flex;align-items:center;font-size:17px;color:#444;height:24px;white-space:nowrap}
.head::after{content:"";flex:1;height:8px;background:var(--bar);margin-left:10px}
.box{background:#fff;border:1px solid var(--line);border-bottom:4px solid var(--orange)}
.ph{position:absolute;border:3px solid #fff;box-shadow:0 0 0 1px #ddd}
.t{font-size:15px;color:#333;line-height:1.3}
.ts{font-size:12px;color:#333;line-height:1.3}
.meta{font-size:9px;color:#aaa;margin-top:3px}
.meta b{font-weight:400;margin-left:10px}
.ex{font-size:11px;color:#555;line-height:1.5;margin-top:8px}
.ex a{color:#333;text-decoration:none}
.side .head{font-size:16px}
.field{border:1px solid #ccc;background:#fff;font-size:10px;color:#888;padding:0 8px;display:flex;align-items:center}
.sidelist{font-size:11px;color:#444;line-height:20px;list-style:none;padding:8px 12px}
.sidelist li::before{content:"• ";color:#666}
.sidelogo{position:absolute;left:8px;top:8px;width:260px;height:176px;border:1px solid #ddd;background:linear-gradient(180deg,#ffffff 0%,#ffffff 40%,#1a1212 62%,#1a1212 100%)}
.sidelogo span{position:absolute;left:0;right:0;top:24px;text-align:center;font-family:"Droid Serif",Georgia,serif;font-size:20px;color:#111}
.footer{left:47px;top:2372px;width:1100px;height:75px;background:var(--dark);border-top:4px solid var(--orange);display:flex;align-items:center;padding:0 38px;font-size:10px;color:#bbb}
.totop{left:1110px;top:2407px;width:26px;height:26px;border-radius:50%;background:var(--orange)}
</style>
</head>
<body>
<div class="abs shell"></div>

<div class="abs topbar">
  <span class="date">Sunday , 17 November 2013</span><span>Sign Up for Newsletter</span>
  <div class="socials"><span></span><span></span><span></span><span></span><span></span><span></span><span></span><span></span><span></span><span></span><span></span><span></span><span></span><span></span><span></span><span></span></div>
</div>

<header class="abs header" role="img" aria-label="Header banner artwork in white and black">
  <div class="brand">Simply Marla</div>
  <div class="portrait" role="img" aria-label="Portrait photo of the author"></div>
</header>

<nav class="abs nav">
  <span class="home"><svg width="22" height="20" viewBox="0 0 22 20"><path d="M11 1L1 10h3v9h5v-6h4v6h5v-9h3z" fill="#fff"/></svg></span>
  <a>Articles</a><a>Videos</a><a>Books</a><a>About Marla</a><a>Upcoming Books</a><a>Contact</a><a>Follow Marla</a><a>Invite Friends</a>
</nav>

<div class="abs main"></div>

<div class="abs slider" role="img" aria-label="Featured post image: cottage in a green forest">
  <div class="cap"><h3>Here will be your post title</h3><p>Molestias ultricies, ante quam urna ut volutpat, egestas dolor dui, nec hac ultrices nulla no...</p></div>
  <div class="track"><i></i></div>
</div>

<div class="abs head" style="left:150px;top:830px;width:591px">Article</div>
<div class="abs box" style="left:150px;top:857px;width:591px;height:337px">
  <div class="ph" style="left:20px;top:23px;width:215px;height:143px;background:linear-gradient(180deg,#c9c27a,#3f6a2a)" role="img" aria-label="Sunlit forest photo"></div>
  <div class="abs" style="left:250px;top:26px;width:320px">
    <div class="t">Here will be your post title</div>
    <div class="meta">November 14, 2013<b>Leave a comment</b></div>
    <div class="ex">Molestias ultricies, ante quam urna ut volutpat, egestas dolor dui, nec hac ultrices nulla ... <a>Read More »</a></div>
  </div>
  <div class="abs" style="left:0;top:180px;width:589px;height:150px;background:#f6f6f6;border-top:1px solid #e2e2e2"></div>
  <div class="ph" style="left:22px;top:197px;width:48px;height:48px;background:linear-gradient(#8fbf6a,#3f7a2f)" role="img" aria-label="Post thumbnail"></div>
  <div class="abs" style="left:88px;top:197px"><div class="ts">Here will be your post title</div><div class="meta">November 14, 2013<b>Leave a comment</b></div></div>
  <div class="ph" style="left:312px;top:197px;width:48px;height:48px;background:linear-gradient(#7fb6c8,#c87a3a)" role="img" aria-label="Post thumbnail"></div>
  <div class="abs" style="left:378px;top:197px"><div class="ts">Here will be your post title</div><div class="meta">November 14, 2013<b>Leave a comment</b></div></div>
  <div class="ph" style="left:22px;top:268px;width:48px;height:48px;background:linear-gradient(#9ac46a,#4a7a2a)" role="img" aria-label="Post thumbnail"></div>
  <div class="abs" style="left:88px;top:268px"><div class="ts">Here will be your post title</div><div class="meta">November 14, 2013<b>Leave a comment</b></div></div>
  <div class="ph" style="left:312px;top:268px;width:48px;height:48px;background:linear-gradient(#eee,#d33)" role="img" aria-label="Post thumbnail"></div>
  <div class="abs" style="left:378px;top:268px"><div class="ts">Here will be your post title</div><div class="meta">November 14, 2013<b>Leave a comment</b></div></div>
</div>

<div class="abs head" style="left:150px;top:1229px;width:591px">Videos</div>
<div class="abs box" style="left:150px;top:1254px;width:591px;height:293px">
  <div class="abs" style="left:301px;top:0;width:1px;height:289px;background:#e2e2e2"></div>
  <div class="abs" style="left:302px;top:0;width:287px;height:289px;background:#f6f6f6"></div>
  <div class="ph" style="left:15px;top:17px;width:270px;height:135px;background:linear-gradient(180deg,#e9b26a,#8a7a4a 60%,#6a6a3a)" role="img" aria-label="Hills at sunset video thumbnail"></div>
  <div class="abs" style="left:15px;top:170px;width:275px">
    <div class="t">Here will be your Video title</div>
    <div class="meta">November 14, 2013<b>Leave a comment</b></div>
    <div class="ex">Molestias ultricies, ante quam urna ut volutpat, egestas dolor dui, nec hac ultrices nulla ... <a>Read More »</a></div>
  </div>
  <div class="ph" style="left:322px;top:14px;width:48px;height:48px;background:linear-gradient(#e08a3a,#2a1a10)" role="img" aria-label="Video thumbnail"></div>
  <div class="abs" style="left:386px;top:12px"><div class="ts">Here will be your Video title</div><div class="meta">November 14, 2013<b>Leave a comment</b></div></div>
  <div class="ph" style="left:322px;top:85px;width:48px;height:48px;background:linear-gradient(#f0a050,#6a3a8a)" role="img" aria-label="Video thumbnail"></div>
  <div class="abs" style="left:386px;top:83px"><div class="ts">Here will be your Video title</div><div class="meta">November 14, 2013<b>Leave a comment</b></div></div>
  <div class="ph" style="left:322px;top:156px;width:48px;height:48px;background:linear-gradient(#8fbf6a,#3f7a2f)" role="img" aria-label="Video thumbnail"></div>
  <div class="abs" style="left:386px;top:154px"><div class="ts">Here will be your Video title</div><div class="meta">November 14, 2013<b>Leave a comment</b></div></div>
  <div class="ph" style="left:322px;top:227px;width:48px;height:48px;background:linear-gradient(#b04aa0,#2a1a5a)" role="img" aria-label="Video thumbnail"></div>
  <div class="abs" style="left:386px;top:225px"><div class="ts">Here will be your Video title</div><div class="meta">November 14, 2013<b>Leave a comment</b></div></div>
</div>

<div class="abs head" style="left:150px;top:1580px;width:591px">Article Scrolling Box</div>
<div class="abs box" style="left:150px;top:1607px;width:591px;height:227px">
  <div class="ph" style="left:24px;top:27px;width:117px;height:56px;background:linear-gradient(#cfd28a,#3f7a2f)" role="img" aria-label="Forest photo"></div>
  <div class="ph" style="left:163px;top:27px;width:117px;height:56px;background:linear-gradient(#9ccf7a,#4a7a2a)" role="img" aria-label="Cottage illustration"></div>
  <div class="ph" style="left:303px;top:27px;width:117px;height:56px;background:linear-gradient(#7fc0d8,#c87a3a)" role="img" aria-label="Animal photo"></div>
  <div class="ph" style="left:442px;top:27px;width:117px;height:56px;background:linear-gradient(#d8a870,#5a3a20)" role="img" aria-label="Tree house photo"></div>
  <div class="abs ts" style="left:20px;top:100px;width:115px">Here will be your post title<div class="meta">November 14, 2013</div></div>
  <div class="abs ts" style="left:159px;top:100px;width:115px">Here will be your post title<div class="meta">November 14, 2013</div></div>
  <div class="abs ts" style="left:299px;top:100px;width:115px">Here will be your post title<div class="meta">November 14, 2013</div></div>
  <div class="abs ts" style="left:438px;top:100px;width:115px">Here will be your post title<div class="meta">November 14, 2013</div></div>
  <svg class="abs" style="left:283px;top:207px" width="22" height="10"><circle cx="5" cy="5" r="4" fill="#888"/><circle cx="17" cy="5" r="4" fill="#ccc"/></svg>
</div>

<div class="abs head" style="left:150px;top:1871px;width:591px">Recent Posts</div>
<div class="abs box" style="left:150px;top:1899px;width:591px;height:404px">
  <div class="ph" style="left:22px;top:25px;width:168px;height:79px;background:linear-gradient(#e9b26a,#6a6a3a)" role="img" aria-label="Hills at sunset"></div>
  <div class="ph" style="left:210px;top:25px;width:168px;height:79px;background:linear-gradient(#e08a3a,#2a1a10)" role="img" aria-label="Tree at sunset"></div>
  <div class="ph" style="left:396px;top:25px;width:168px;height:79px;background:linear-gradient(#f0a050,#6a3a8a)" role="img" aria-label="Beach sunset"></div>
  <div class="abs ts" style="left:20px;top:124px">Here will be your Video title<div class="meta">November 14, 2013</div></div>
  <div class="abs ts" style="left:208px;top:124px">Here will be your Video title<div class="meta">November 14, 2013</div></div>
  <div class="abs ts" style="left:394px;top:124px">Here will be your Video title<div class="meta">November 14, 2013</div></div>
  <div class="ph" style="left:22px;top:205px;width:168px;height:79px;background:linear-gradient(#9ccf7a,#4a7a2a)" role="img" aria-label="Cottage illustration"></div>
  <div class="ph" style="left:210px;top:205px;width:168px;height:79px;background:linear-gradient(#b04aa0,#2a1a5a)" role="img" aria-label="Purple sunset"></div>
  <div class="ph" style="left:396px;top:205px;width:168px;height:79px;background:linear-gradient(#e0e0e0,#a09070)" role="img" aria-label="Fence in a field"></div>
  <div class="abs ts" style="left:20px;top:306px">Here will be your Video title<div class="meta">November 14, 2013</div></div>
  <div class="abs ts" style="left:208px;top:306px">Here will be your Video title<div class="meta">November 14, 2013</div></div>
  <div class="abs ts" style="left:394px;top:306px">Here will be your Video title<div class="meta">November 14, 2013</div></div>
</div>

<div class="side">
  <div class="abs" style="left:763px;top:514px;width:278px;height:8px;background:var(--bar)"></div>
  <div class="abs box" style="left:763px;top:531px;width:278px;height:200px">
    <div class="sidelogo" role="img" aria-label="Site banner artwork in white and black"><span>Simply Marla</span></div>
  </div>
  <div class="abs field" style="left:763px;top:757px;width:278px;height:34px">to search type and hit enter</div>

  <div class="abs head" style="left:763px;top:820px;width:278px">Follow us on Circlenet</div>
  <div class="abs box" style="left:763px;top:853px;width:278px;height:96px">
    <div class="abs" style="left:18px;top:4px;width:240px;height:82px;border:1px solid #ddd"></div>
    <div class="abs" style="left:18px;top:4px;width:90px;height:82px;background:var(--red);color:#fff;font-size:13px;display:flex;align-items:flex-end;justify-content:center;padding-bottom:6px">k7folio</div>
    <div class="abs" style="left:118px;top:10px;font-size:13px">k7folio</div>
    <div class="abs" style="left:118px;top:42px;width:26px;height:22px;background:var(--red)"></div>
    <div class="abs" style="left:150px;top:42px;width:56px;height:22px;border:1px solid #ccc;font-size:10px;display:flex;align-items:center;justify-content:center">Follow</div>
    <div class="abs" style="left:212px;top:42px;width:30px;height:22px;border:1px solid #ccc;font-size:10px;display:flex;align-items:center;justify-content:center">+1</div>
  </div>

  <div class="abs head" style="left:763px;top:974px;width:278px">Featured Video</div>
  <div class="abs box" style="left:763px;top:1007px;width:278px;height:193px">
    <div class="abs" style="left:10px;top:0;width:256px;height:185px;background:linear-gradient(180deg,#3a3a3a,#a07060 45%,#d8d0c0 70%,#222)" role="img" aria-label="Music video still"></div>
    <div class="abs" style="left:10px;top:0;width:256px;height:22px;background:rgba(0,0,0,.75);color:#fff;font-size:10px;padding:4px 8px;white-space:nowrap;overflow:hidden">Nova Reyes - Run Bright (Official Video)</div>
    <div class="abs" style="left:120px;top:80px;width:36px;height:26px;background:rgba(0,0,0,.8);border-radius:5px"><svg width="36" height="26"><path d="M14 7l10 6-10 6z" fill="#fff"/></svg></div>
    <div class="abs" style="left:10px;top:163px;width:256px;height:22px;background:#1b1b1b;color:#ccc;font-size:9px;padding:5px 8px">▶ &nbsp;0:00 / 6:32</div>
  </div>

  <div class="abs box" style="left:763px;top:1232px;width:278px;height:187px;background:linear-gradient(180deg,#e8a040,#5a2a10 70%,#1a0a05)" role="img" aria-label="Tree at sunset video image">
    <div class="abs" style="left:0;bottom:0;width:276px;height:28px;background:rgba(0,0,0,.7);color:#fff;font-size:14px;padding:4px 8px">Here will be your Video title</div>
  </div>

  <div class="abs head" style="left:763px;top:1435px;width:278px">Login</div>
  <div class="abs box" style="left:763px;top:1462px;width:278px;height:165px;background:#f6f6f6">
    <div class="abs field" style="left:20px;top:15px;width:238px;height:28px">Username</div>
    <div class="abs field" style="left:20px;top:52px;width:238px;height:28px">••••••••</div>
    <div class="abs" style="left:20px;top:92px;width:58px;height:26px;border:1px solid #bbb;background:#f0f0f0;font-size:11px;display:flex;align-items:center;justify-content:center">Log in</div>
    <div class="abs" style="left:92px;top:97px;font-size:10px">☑ Remember Me</div>
    <div class="abs" style="left:20px;top:134px;font-size:10px">• &nbsp;Lost your password?</div>
  </div>

  <div class="abs head" style="left:763px;top:1653px;width:278px">Product</div>
  <div class="abs box" style="left:763px;top:1682px;width:278px;height:84px;padding:8px 10px">
    <div style="font-size:10px;font-weight:700;line-height:1.3;width:220px">The Lantern Circle: Spies of the Harbor War</div>
    <div style="font-size:10px;margin-top:6px"><s>£987</s> <u>£687</u></div>
    <div class="abs" style="left:240px;top:8px;width:28px;height:30px;background:linear-gradient(#8a7a60,#3a2a1a)" role="img" aria-label="Book cover"></div>
  </div>

  <div class="abs head" style="left:763px;top:1792px;width:278px">Recent Comments</div>
  <div class="abs box" style="left:763px;top:1815px;width:278px;height:45px"><ul class="sidelist" style="padding-top:4px"><li>admin on Newsletter</li></ul></div>

  <div class="abs head" style="left:763px;top:1887px;width:278px">Recent Posts</div>
  <div class="abs box" style="left:763px;top:1911px;width:278px;height:120px">
    <ul class="sidelist" style="padding-top:4px"><li>Here will be your Video title</li><li>Here will be your Video title</li><li>Here will be your Video title</li><li>Here will be your Video title</li><li>Here will be your Video title</li></ul>
  </div>

  <div class="abs box" style="left:763px;top:2053px;width:278px;height:187px;border-bottom:none;background:linear-gradient(160deg,#f4f4f4 30%,#e33 45%,#ccc 70%)" role="img" aria-label="Red umbrellas photo">
    <div class="abs" style="left:0;bottom:0;width:276px;height:28px;background:rgba(0,0,0,.7);color:#fff;font-size:14px;padding:4px 8px">Here will be your post title</div>
  </div>
</div>

<footer class="abs footer">
  <span>©2013 Simply Marla</span>
  <div class="socials"><span></span><span></span><span></span><span></span><span></span><span></span><span></span><span></span><span></span><span></span><span></span><span></span><span></span><span></span><span></span><span></span></div>
</footer>
<div class="abs totop"><svg width="26" height="26"><path d="M8 15l5-5 5 5" fill="none" stroke="#fff" stroke-width="2.5"/></svg></div>
</body>
</html>
```